Design a App to help people have successful dates!

We require an awesome designer to help us with an App design for a new dating app we are introducing! Our App is intended to help Users build confidence is knowing what questions or ask and answer when going on dates! As you can see from our Project Brief, the intent of the app is to display two types of content to the user 1) Dating Questions, and 2) Dating Tips. We have developed wireframes to help convey what each screen should convey. The intent is to 'inform' and 'educate' the User on what questions to ask, or what questions could be asked of them. Also, we would like to include Banner Ads on the 'Question' and 'Tip' screens, which you can see in the brief.

Target Market(s)

Men and women - aged 18 - 45 who need help identifying dating questions

Industry/Entity Type

Dating App

Font styles to use
Sans Serif

Requirements
Must have
• Please review the PDF brief that we have uploaded. Please make the swipe left and right feature modern (I only included the buttons as a guide only). The ‘Romance Prompt Ace’ App is intended to be a light-hearted, simple, elegant, fun App, to help Users ask and engage in dating questions. Think of this app as an 'LoveNest' (high quality, educated Users) to help users with identifying questions to ask on dates.
Nice to have
• Please review the PDF brief that we have uploaded.
Should not have
• The App is intended to only include genuine, legitimate, clean and appropriate content. This is not a 'Flarn' stiyle look-up app.

```html
<!DOCTYPE html>
<html lang="en">
<head>
<meta charset="utf-8">
<title>Romance Prompt Ace – App Screens</title>
<link href="https://fonts.googleapis.com/css2?family=Rubik:wght@300;400;500&display=swap" rel="stylesheet">
<style>
  :root {
    --page: #eef1f6;
    --blue: #4c63f6;
    --blue-light: #6a86ff;
    --red: #e2195a;
    --red-light: #f5606c;
    --ink: #3d4377;
    --white: #ffffff;
    --screen-bg: #eef1f7;
    --dot-blue: #c9d2fb;
    --dot-red: #f7c5d2;
  }
  * { box-sizing: border-box; margin: 0; padding: 0; }
  html, body { width: 1200px; height: 616px; overflow: hidden; }
  body {
    background: var(--page);
    font-family: "Rubik", sans-serif;
    position: relative;
  }
  .screen {
    position: absolute;
    top: 68px;
    width: 212px;
    height: 459px;
    border-radius: 26px;
    overflow: hidden;
    background: var(--screen-bg);
    box-shadow: 0 14px 30px rgba(60, 70, 120, 0.16);
  }
  .screen--welcome { left: 117px; background: linear-gradient(180deg, var(--blue) 0%, var(--blue-light) 100%); }
  .screen--home { left: 374px; }
  .screen--questions { left: 629px; }
  .screen--tips { left: 885px; }

  /* Welcome */
  .welcome__photo {
    position: absolute; left: 0; right: 0; top: 150px; bottom: 0;
    background: linear-gradient(180deg, rgba(110,120,230,0.0) 0%, #7d80d6 35%, #8a7fb8 60%, #5f6be8 100%);
  }
  .brand-mark {
    position: absolute; left: 50%; top: 50px; width: 26px; height: 26px;
    margin-left: -13px; border-radius: 50%; background: var(--white);
  }
  .welcome__title {
    position: absolute; top: 88px; width: 100%; text-align: center;
    color: var(--white); font-weight: 500; font-size: 16px;
  }
  .welcome__tagline {
    position: absolute; top: 115px; width: 100%; text-align: center;
    color: var(--white); font-weight: 300; font-size: 13px;
  }
  .start-btn {
    position: absolute; left: 15px; top: 397px; width: 182px; height: 36px;
    border-radius: 18px; background: var(--white);
    color: var(--ink); font-size: 12px; font-weight: 500;
    display: flex; align-items: center; justify-content: center;
  }
  .start-btn__arrow {
    position: absolute; right: 4px; top: 4px; width: 28px; height: 28px;
    border-radius: 50%; background: #e6eafd;
    display: flex; align-items: center; justify-content: center;
  }

  /* Home */
  .home__photo {
    position: absolute; left: 0; right: 0; top: 40px; height: 260px;
    background: radial-gradient(circle at 70% 60%, #4d5a86 0%, #2a3352 55%, #1c2238 100%);
  }
  .header-wave { position: absolute; left: 0; top: 0; width: 212px; }
  .header-title {
    position: absolute; top: 32px; left: 0; width: 100%;
    display: flex; align-items: center; justify-content: center; gap: 6px;
    color: var(--white); font-size: 12px; font-weight: 500;
  }
  .home__panel {
    position: absolute; left: 0; right: 0; top: 273px; bottom: 0;
    background: var(--screen-bg); border-radius: 26px 26px 0 0;
  }
  .menu-btn {
    position: absolute; left: 14px; width: 182px; height: 47px; border-radius: 24px;
    color: var(--white); font-size: 12px; font-weight: 500;
    display: flex; align-items: center; justify-content: center; gap: 7px;
  }
  .menu-btn--questions { top: 298px; background: linear-gradient(90deg, var(--blue), var(--blue-light)); box-shadow: 0 8px 14px rgba(76,99,246,0.3); }
  .menu-btn--tips { top: 374px; background: linear-gradient(90deg, var(--red), var(--red-light)); box-shadow: 0 8px 14px rgba(226,25,90,0.3); }
  .icon-dot {
    width: 14px; height: 14px; border-radius: 50%; background: var(--white);
    display: inline-flex; align-items: center; justify-content: center;
    font-size: 8px; font-weight: 500; line-height: 1;
  }
  .icon-dot--blue { color: var(--blue); }
  .icon-dot--red { color: var(--red); }

  /* Card screens */
  .nav-title {
    position: absolute; top: 26px; left: 16px; right: 0;
    display: flex; align-items: center; color: var(--white);
    font-size: 12px; font-weight: 500;
  }
  .nav-title .back { width: 10px; margin-right: 24px; }
  .nav-title .icon-dot { margin-right: 9px; }
  .card-peek {
    position: absolute; top: 145px; width: 21px; height: 151px;
    background: var(--white); border-radius: 10px;
  }
  .card-peek--left { left: 0; border-radius: 0 10px 10px 0; }
  .card-peek--right { right: 0; border-radius: 10px 0 0 10px; }
  .card {
    position: absolute; left: 34px; top: 111px; width: 143px; height: 215px;
    background: var(--white); border-radius: 18px; overflow: hidden;
    box-shadow: 0 10px 20px rgba(60, 70, 120, 0.15);
  }
  .card__head { position: absolute; left: 0; top: 0; width: 143px; height: 82px; }
  .card__badge {
    position: absolute; left: 56px; top: 14px; width: 31px; height: 31px;
    border-radius: 50%; background: var(--white); color: var(--blue);
    display: flex; align-items: center; justify-content: center;
    font-size: 13px; font-weight: 500;
  }
  .card__heading {
    position: absolute; top: 20px; width: 100%; padding: 0 10px; text-align: center;
    color: var(--white); font-size: 9px; font-weight: 500; line-height: 1.3;
  }
  .card__question {
    position: absolute; top: 89px; width: 100%; text-align: center;
    color: var(--ink); font-size: 11px; font-weight: 500; line-height: 1.3; padding: 0 14px;
  }
  .card__body {
    position: absolute; top: 88px; width: 100%; text-align: center;
    color: var(--ink); font-size: 8.6px; font-weight: 500; line-height: 1.35; padding: 0 10px;
  }
  .pager {
    position: absolute; top: 355px; left: 0; width: 100%;
    display: flex; justify-content: center; gap: 4px;
  }
  .pager span { width: 5px; height: 5px; border-radius: 50%; }
  .pager--blue span { background: var(--dot-blue); }
  .pager--blue span.is-active { background: var(--blue); }
  .pager--red span { background: var(--dot-red); }
  .pager--red span.is-active { background: var(--red); }
  .ad-banner {
    position: absolute; left: 0; right: 0; top: 423px; height: 36px;
    background: linear-gradient(90deg, #3c6c8c 0%, #b07a3a 45%, #d9b04a 80%, #e08a2a 100%);
  }
</style>
</head>
<body>

<section class="screen screen--welcome">
  <div class="welcome__photo" role="img" aria-label="Photo of a couple walking hand in hand along a city street at dusk"></div>
  <div class="brand-mark"></div>
  <h1 class="welcome__title">Romance Prompt Ace</h1>
  <p class="welcome__tagline">No awkward silences</p>
  <div class="start-btn">Get Started
    <span class="start-btn__arrow">
      <svg width="8" height="12" viewBox="0 0 8 12"><path d="M1.5 1.5 6 6l-4.5 4.5" fill="none" stroke="#3d4377" stroke-width="2" stroke-linecap="round" stroke-linejoin="round"/></svg>
    </span>
  </div>
</section>

<section class="screen screen--home">
  <div class="home__photo" role="img" aria-label="Photo of a couple holding candles at night with string lights"></div>
  <svg class="header-wave" height="110" viewBox="0 0 212 110" aria-hidden="true">
    <defs><linearGradient id="hb" x1="0" x2="1"><stop offset="0" stop-color="#4c63f6"/><stop offset="1" stop-color="#5b74fb"/></linearGradient></defs>
    <path d="M0 0H212V100C198 80 175 68 140 66C100 64 70 72 40 68C20 65 8 58 0 50Z" fill="url(#hb)"/>
  </svg>
  <div class="header-title"><span class="icon-dot icon-dot--blue"></span>Romance Prompt Ace</div>
  <div class="home__panel"></div>
  <div class="menu-btn menu-btn--questions"><span class="icon-dot icon-dot--blue">??</span>Dating Questions</div>
  <div class="menu-btn menu-btn--tips"><span class="icon-dot icon-dot--red">i</span>Dating Tips</div>
</section>

<section class="screen screen--questions">
  <svg class="header-wave" height="100" viewBox="0 0 212 100" aria-hidden="true">
    <path d="M0 0H212V92C196 70 172 64 140 64C100 64 70 70 40 66C20 63 8 56 0 48Z" fill="#4c63f6"/>
  </svg>
  <div class="nav-title">
    <svg class="back" width="8" height="12" viewBox="0 0 8 12"><path d="M6.5 1.5 2 6l4.5 4.5" fill="none" stroke="#fff" stroke-width="2" stroke-linecap="round" stroke-linejoin="round"/></svg>
    <span class="icon-dot icon-dot--blue">??</span>Dating Questions
  </div>
  <div class="card-peek card-peek--left"></div>
  <div class="card-peek card-peek--right"></div>
  <article class="card">
    <svg class="card__head" viewBox="0 0 143 82" aria-hidden="true">
      <defs><linearGradient id="qc" x1="0" x2="1"><stop offset="0" stop-color="#5a74fb"/><stop offset="1" stop-color="#4c63f6"/></linearGradient></defs>
      <path d="M0 0H143V82C140 70 132 62 118 62H0Z" fill="url(#qc)"/>
    </svg>
    <div class="card__badge">??</div>
    <p class="card__question">What makes you laugh?</p>
  </article>
  <div class="pager pager--blue"><span></span><span></span><span></span><span></span><span class="is-active"></span><span></span><span></span><span></span><span></span><span></span><span></span><span></span></div>
  <div class="ad-banner" role="img" aria-label="Banner advertisement for the mobile game Harbor Clash"></div>
</section>

<section class="screen screen--tips">
  <svg class="header-wave" height="100" viewBox="0 0 212 100" aria-hidden="true">
    <defs><linearGradient id="rh" x1="0" x2="1"><stop offset="0" stop-color="#e2195a"/><stop offset="1" stop-color="#f04a66"/></linearGradient></defs>
    <path d="M0 0H212V92C196 70 172 64 140 64C100 64 70 70 40 66C20 63 8 56 0 48Z" fill="url(#rh)"/>
  </svg>
  <div class="nav-title">
    <svg class="back" width="8" height="12" viewBox="0 0 8 12"><path d="M6.5 1.5 2 6l4.5 4.5" fill="none" stroke="#fff" stroke-width="2" stroke-linecap="round" stroke-linejoin="round"/></svg>
    <span class="icon-dot icon-dot--red">i</span>Dating Tips
  </div>
  <div class="card-peek card-peek--left"></div>
  <div class="card-peek card-peek--right"></div>
  <article class="card">
    <svg class="card__head" viewBox="0 0 143 82" aria-hidden="true">
      <defs><linearGradient id="tc" x1="0" x2="1"><stop offset="0" stop-color="#e2195a"/><stop offset="1" stop-color="#ee3f62"/></linearGradient></defs>
      <path d="M0 0H143V82C140 70 132 62 118 62H0Z" fill="url(#tc)"/>
    </svg>
    <p class="card__heading">Arrive to the date<br>on time.</p>
    <p class="card__body">Don’t be one of those ‘fashionably late’ people. Your date may feel nervous or anxious whether you are even coming. Make sure you arrive to meet your date on time.</p>
  </article>
  <div class="pager pager--red"><span></span><span></span><span></span><span></span><span class="is-active"></span><span></span><span></span><span></span><span></span><span></span><span></span><span></span></div>
  <div class="ad-banner" role="img" aria-label="Banner advertisement for the mobile game Harbor Clash"></div>
</section>

</body>
</html>
```